Business Card Design Project

We are rebranding an existing automotive collision repair business. The business is called dentworks garage. I have attached logo but I'm not tied to that. I want to leave this wide open.

I want this card to say we are professional, competent, cutting edge. We are focused on customers and use a lot of the latest technology to make the customer experience different. We sign customers in on iPads. Paperwork I signed electronically and updates are sent via text, email, logging on a website or as they wish. I want this innovation and image to come through in our cards

Target Market(s)

60%. Women 40% men. Age 35-60

Industry/Entity Type

Automotive

Requirements
Must have
• The card must have name, title, phone,email, cell, web page

```html
<!DOCTYPE html>
<html lang="en">
<head>
<meta charset="utf-8">
<title>Dentworks Garage – Business Card</title>
<link href="https://fonts.googleapis.com/css2?family=Open+Sans:wght@400;600;700&display=swap" rel="stylesheet">
<style>
  :root {
    --bg: #3a3a3a;
    --card-white: #ffffff;
    --green-dark: #1f7a2a;
    --green-mid: #4ea624;
    --green-light: #86c226;
    --text-grey: #6d6d6d;
    --text-dark: #1a1a1a;
    --icon-green: #6fb52c;
  }
  * { margin: 0; padding: 0; box-sizing: border-box; }
  html, body { width: 1200px; height: 900px; overflow: hidden; }
  body {
    background: var(--bg);
    font-family: "Open Sans", Arial, sans-serif;
    position: relative;
  }
  .card {
    position: absolute;
    width: 580px;
    height: 330px;
    border-radius: 26px;
    overflow: hidden;
    box-shadow: 0 12px 30px rgba(0,0,0,0.45);
  }
  /* Back side */
  .card--back {
    left: 560px;
    top: 70px;
    background: linear-gradient(100deg, var(--green-dark) 0%, var(--green-mid) 45%, var(--green-light) 100%);
  }
  .card--back .brand-name {
    position: absolute;
    left: 0; right: 0; top: 128px;
    text-align: center;
    font-weight: 700;
    font-size: 46px;
    color: #ffffff;
    letter-spacing: -0.5px;
  }
  .card--back .web {
    position: absolute;
    left: 0; right: 0; bottom: 30px;
    text-align: center;
    font-size: 18px;
    color: #ffffff;
    letter-spacing: 0.5px;
  }
  /* Front side */
  .card--front {
    left: 60px;
    top: 500px;
    background: var(--card-white);
  }
  .card--front .swoosh {
    position: absolute;
    inset: 0;
    width: 580px;
    height: 330px;
  }
  .front-brand {
    position: absolute;
    left: 34px;
    top: 28px;
    font-weight: 700;
    font-size: 28px;
    color: var(--green-mid);
    letter-spacing: -0.3px;
  }
  .address {
    position: absolute;
    left: 36px;
    top: 78px;
    font-size: 14px;
    line-height: 19px;
    color: var(--text-grey);
  }
  .contact-list {
    position: absolute;
    left: 36px;
    top: 126px;
    list-style: none;
    font-size: 14px;
    line-height: 20px;
    color: var(--text-grey);
  }
  .contact-list li { display: flex; align-items: center; gap: 8px; }
  .contact-list svg { width: 12px; height: 12px; flex: none; }
  .person {
    position: absolute;
    right: 44px;
    top: 160px;
    text-align: right;
  }
  .person .name {
    font-weight: 600;
    font-size: 22px;
    color: var(--text-dark);
  }
  .person .title {
    font-size: 15px;
    color: var(--text-grey);
    margin-top: 2px;
  }
</style>
</head>
<body>

<section class="card card--back" aria-label="Business card back">
  <div class="brand-name">Dentworks Garage</div>
  <div class="web">www.dentworksgarage.com</div>
</section>

<section class="card card--front" aria-label="Business card front">
  <svg class="swoosh" viewBox="0 0 580 330" aria-hidden="true">
    <defs>
      <linearGradient id="bandGreen" x1="0" y1="0" x2="1" y2="0">
        <stop offset="0" stop-color="#86c226"/>
        <stop offset="0.7" stop-color="#5fae24"/>
        <stop offset="1" stop-color="#1f7a2a"/>
      </linearGradient>
      <linearGradient id="bandSilver" x1="0" y1="0" x2="1" y2="0">
        <stop offset="0" stop-color="#111111"/>
        <stop offset="0.35" stop-color="#9a9a9a"/>
        <stop offset="1" stop-color="#e6e6e6"/>
      </linearGradient>
    </defs>
    <path d="M0 232 C 150 262, 330 300, 580 262 L580 330 L0 330 Z" fill="url(#bandGreen)"/>
    <path d="M0 232 C 150 262, 330 300, 560 300 C 330 292, 150 270, 0 250 Z" fill="url(#bandSilver)"/>
    <path d="M0 250 C 150 270, 330 292, 560 300 C 330 302, 150 284, 0 262 Z" fill="#ffffff" opacity="0.9"/>
  </svg>

  <div class="front-brand">Dentworks Garage</div>

  <p class="address">4710 N. Ridgeview Drive. STE 12<br>Unit 3 Tempe, AZ 85281</p>

  <ul class="contact-list">
    <li>
      <svg viewBox="0 0 12 12"><path d="M2 1 L4.5 1 L5.5 3.5 L4 4.8 C4.8 6.5 5.6 7.3 7.2 8 L8.5 6.5 L11 7.5 L11 10 C6 10.5 1.5 6 2 1 Z" fill="var(--icon-green)"/></svg>
      800-555-0142
    </li>
    <li>
      <svg viewBox="0 0 12 12"><rect x="1" y="8" width="2" height="3" fill="var(--icon-green)"/><rect x="4" y="6" width="2" height="5" fill="var(--icon-green)"/><rect x="7" y="4" width="2" height="7" fill="var(--icon-green)"/><rect x="10" y="2" width="2" height="9" fill="var(--icon-green)"/></svg>
      800-555-0178
    </li>
    <li>
      <svg viewBox="0 0 12 12"><rect x="1" y="2.5" width="10" height="7" fill="none" stroke="var(--icon-green)" stroke-width="1.2"/><path d="M1 2.5 L6 6.5 L11 2.5" fill="none" stroke="var(--icon-green)" stroke-width="1.2"/></svg>
      info@dentworksgarage.com
    </li>
    <li>
      <svg viewBox="0 0 12 12"><circle cx="6" cy="6" r="5" fill="none" stroke="var(--icon-green)" stroke-width="1.2"/><ellipse cx="6" cy="6" rx="2.2" ry="5" fill="none" stroke="var(--icon-green)" stroke-width="1"/><line x1="1" y1="6" x2="11" y2="6" stroke="var(--icon-green)" stroke-width="1"/></svg>
      www.dentworksgarage.com
    </li>
  </ul>

  <div class="person">
    <div class="name">Daniel Reyes</div>
    <div class="title">Vice President</div>
  </div>
</section>

</body>
</html>
```